Marlowvale Wholefoods web design

Go to marlowvalewholefoods.com.au an using the current layout create a design that will attract customers to this wholefood website.

You may suggest / make slight changes to the layout to create effective graphic design principles.

The LOGO design is TM already. So no changes there. Second logo attached is authorised for use and is a area branding LOGO.

Colours need to reflect health and wellbeing.

Don't want Medical style or New age.
Updates

Thank you for your submissions so far. I have sent them out to a trusty panel of friends to hear what they have to say. Some of you have done very well.

Reason: There are a few submissions outstanding. I will eliminate a few designs today and give feed back. Thankyou

Thank you for your submissions so far I will not be asking for more design submissions from other designers. The ones I have are under consideration and there are a few minor changes to each that may just bring out the one that is IT! The two designs I have narrowed it down to are very different in approach so please bear with me a couple more days. Thank you.

Target Market(s)

Whole food health concious people target market locally Home Delivery would be young Mums with restricted movement because of young children. Older people that are restricted transport users.

Busy commuters that leave our area for work and just want to relax on the weekend with their family and local bush walking or garden activities.

Industry/Entity Type

Graphic Design

Requirements
Should not have
• Medical or sterile hospital feel. New age or too alternative living feel.

```html
<!DOCTYPE html>
<html lang="en">
<head>
<meta charset="utf-8">
<title>Marlowvale Wholefoods</title>
<link href="https://fonts.googleapis.com/css2?family=Arimo:wght@400;700&family=Roboto+Slab:wght@700&family=Roboto+Condensed:wght@400;700&family=Ubuntu:wght@400;500&family=Roboto+Serif:wght@700&display=swap" rel="stylesheet">
<style>
:root{
  --green:#6cb52d;
  --green-text:#62a726;
  --red:#e3231b;
  --purple:#6a2a78;
  --ink:#222;
  --text:#444;
  --line:#d8d8d8;
  --panel:#f7f7f7;
  --footer:#353535;
  --white:#fff;
}
*{box-sizing:border-box;margin:0;padding:0}
html,body{width:862px;height:1200px;overflow:hidden;background:var(--white)}
body{position:relative;font-family:"Arimo",Arial,sans-serif;color:var(--text)}
h2{font-weight:400}
.abs{position:absolute}

/* header */
.brand{left:70px;top:28px;width:130px;height:74px;display:flex;align-items:center;gap:8px}
.brand-dot{width:22px;height:22px;border-radius:50%;background:var(--green);flex:none}
.brand-name{font-family:"Ubuntu",sans-serif;font-weight:500;font-size:15px;line-height:18px;color:var(--purple)}
.search{left:429px;top:29px;width:177px;height:19px;border:1px solid #cfcfcf;border-radius:3px;background:#f1f1f1;box-shadow:inset 0 1px 2px rgba(0,0,0,.15);font-size:9.5px;color:#999;padding:4px 9px}
.search svg{position:absolute;right:6px;top:3px}
.account{left:624px;top:32px;font-size:10px;color:var(--ink);white-space:nowrap}
.nav{left:354px;top:75px;width:435px;display:flex;justify-content:space-between;font-size:10.5px;letter-spacing:.2px;color:var(--ink)}
.nav .active{color:var(--green-text)}

/* hero */
.hero{left:71px;top:117px;width:719px;height:278px;border-radius:6px;overflow:hidden;box-shadow:0 1px 4px rgba(0,0,0,.3);
  background:
    linear-gradient(180deg,rgba(0,0,0,0) 0%,rgba(0,0,0,0) 72%,rgba(214,92,38,.55) 86%,rgba(190,60,30,.6) 100%),
    linear-gradient(90deg,#b52a1c 0%,#c63a22 10%,#d06a22 20%,#7c8f35 30%,#a7b071 36%,#e9e6df 44%,#f3efe9 52%,#dfe6ee 60%,#c6d6e8 70%,#f0ece6 80%,#d9cdbd 90%,#c6b7a0 100%)}
.hero-title{left:83px;top:158px;font-family:"Roboto Slab",serif;font-weight:700;font-size:17.5px;color:var(--white);text-shadow:0 1px 3px rgba(0,0,0,.6);white-space:nowrap}
.hero-rule{left:84px;top:189px;width:326px;height:1px;background:rgba(255,255,255,.85)}
.hero-star{left:229px;top:182px}
.register{left:146px;top:206px;width:179px;height:189px;background:var(--white);border:3px solid #8ab45a;border-bottom:none}
.register h2{position:absolute;left:15px;top:17px;font-family:"Roboto Condensed",sans-serif;font-weight:700;font-size:16px;color:#555}
.field{position:absolute;left:15px;width:145px;height:24px;background:#eee;border:1px solid #bbb;font-family:"Roboto Condensed",sans-serif;font-size:7.5px;color:#555;padding:7px 7px}
.enter{position:absolute;left:15px;top:102px;width:145px;height:25px;background:var(--red);color:var(--white);font-family:"Roboto Condensed",sans-serif;font-weight:700;font-size:11px;text-align:center;line-height:25px}
.reg-note{position:absolute;left:17px;font-family:"Roboto Condensed",sans-serif;font-size:7px;color:#444}

/* section heads */
.section-head{font-family:"Ubuntu",sans-serif;font-weight:400;font-size:17px;color:var(--green-text)}
.section-rule{height:3px;border-top:1px solid var(--line);border-bottom:1px solid var(--line)}

/* photo fills */
.seeds{background:linear-gradient(160deg,#8f8072 0%,#6e5f52 35%,#9a8b7c 65%,#7a6a5b 100%)}
.bottle{background:linear-gradient(90deg,#f6f6f6 0%,#f6f6f6 36%,#2e4f8e 40%,#2e4f8e 60%,#f6f6f6 64%,#f6f6f6 100%)}
.almonds{background:linear-gradient(180deg,#f2f2f2 0%,#b77a47 18%,#9a5f33 55%,#b98150 82%,#efefef 100%)}
.pantry{background:linear-gradient(90deg,#3a3a3a 0%,#8d8d8d 25%,#4a4a4a 50%,#9a9a9a 75%,#555 100%)}
.balls{background:linear-gradient(180deg,#c7a173 0%,#6e5a54 25%,#7a6660 65%,#7e2b1f 88%,#b98a5e 100%)}
.grain{background:linear-gradient(150deg,#a89b6e 0%,#958a5c 50%,#a59870 100%)}

/* deals */
.deal{width:143px;height:107px;background:var(--white);border:2px solid #ddd;padding:2px;box-shadow:0 7px 6px -5px rgba(0,0,0,.25)}
.deal .pic{width:100%;height:100%}
.price{position:absolute;left:2px;right:2px;bottom:2px;height:21px;background:rgba(40,40,40,.78);color:var(--white);font-family:"Roboto Condensed",sans-serif;font-weight:700;font-size:12px;line-height:21px;padding-left:30px}
.price svg{position:absolute;right:24px;top:4px}

/* news */
.news{width:139px;height:172px;background:var(--white);border:1px solid #ddd;box-shadow:0 1px 3px rgba(0,0,0,.15)}
.news .pic{position:absolute;left:6px;top:8px;width:126px;height:80px}
.news p{position:absolute;left:4px;right:4px;top:99px;font-size:8.5px;line-height:13px;text-align:center;color:#333}
.news a{position:absolute;right:12px;top:145px;font-family:"Roboto Serif",serif;font-weight:700;font-size:8px;color:var(--green-text);text-decoration:none}

/* sidebar */
.tab{width:160px;height:24px;background:var(--green);color:var(--white);font-family:"Ubuntu",sans-serif;font-weight:500;font-size:12.5px;text-align:center;line-height:26px}
.cats{width:177px;background:var(--panel);border:1px solid #eee;padding:9px 10px 0}
.cats li{list-style:none;height:24.4px;border-bottom:1px solid #e2e2e2;font-size:10px;color:#333;padding:6px 0 0 20px;letter-spacing:.2px}
.cats li:last-child{border-bottom:none}

/* newsletter */
.sub-title{left:90px;top:1058px;font-family:"Roboto Condensed",sans-serif;font-size:15px;color:var(--green-text)}
.sub-title span{color:var(--purple)}
.sub-input{top:1057px;width:232px;height:23px;background:#ececec;border:1px solid #c9c9c9;border-radius:7px;box-shadow:inset 0 1px 2px rgba(0,0,0,.12);font-size:9px;color:#555;padding:6px 10px}
.submit{left:715px;top:1057px;width:60px;height:23px;border-radius:8px;background:linear-gradient(#4aa52b,#2e8419);border:1px solid #2b7a18;color:var(--white);font-size:11px;text-align:center;line-height:21px}

/* footer */
.footer{left:0;top:1110px;width:862px;height:90px;background:var(--footer);border-top:3px solid var(--green)}
.foot-links{left:73px;top:1127px;font-size:8px;color:var(--white);white-space:nowrap;word-spacing:1px}
.copy{left:73px;top:1144px;font-size:8.5px;color:var(--white);white-space:nowrap}
.cards{left:72px;top:1164px;display:flex;gap:7px}
.cards span{width:26px;height:16px;border-radius:2px;background:#ddd}
.cards .wide{width:58px;background:#8fb0d8}
.area{left:680px;top:1128px;width:100px;color:#eee;font-family:"Ubuntu",sans-serif}
.area .name{font-size:14px;line-height:16px}
.area .tag{font-size:7px;margin-top:2px}
</style>
</head>
<body>

<header>
  <div class="abs brand"><span class="brand-dot"></span><span class="brand-name">Marlowvale Wholefoods</span></div>
  <div class="abs search">Search here
    <svg width="11" height="11" viewBox="0 0 11 11"><circle cx="4.5" cy="4.5" r="3.3" fill="none" stroke="#222" stroke-width="1.6"/><line x1="7" y1="7" x2="10" y2="10" stroke="#222" stroke-width="1.8"/></svg>
  </div>
  <div class="abs account">My Account &nbsp;&nbsp;|&nbsp; 0 items in your Cart</div>
  <nav class="abs nav"><span class="active">HOME</span><span>SHOP</span><span>PURCHASE BY WEIGHT</span><span>RECIPES</span><span>BLOG</span><span>CONTACT US</span></nav>
</header>

<section>
  <div class="abs hero" role="img" aria-label="Photo of a family preparing fresh vegetables in a bright kitchen beside a market produce display"></div>
  <div class="abs hero-title">THE BEST WHOLE FOOD SUPPLIERS</div>
  <div class="abs hero-rule"></div>
  <svg class="abs hero-star" width="12" height="12" viewBox="0 0 12 12"><polygon points="6,0 7.6,4.2 12,4.4 8.5,7.1 9.7,11.5 6,9 2.3,11.5 3.5,7.1 0,4.4 4.4,4.2" fill="#fff"/></svg>
  <div class="abs register">
    <h2>Register Now</h2>
    <div class="field" style="top:47px">User name</div>
    <div class="field" style="top:77px">Password</div>
    <div class="enter">ENTER HERE</div>
    <div class="reg-note" style="top:139px">In Not registered? | Do it here!</div>
    <div class="reg-note" style="top:153px">Forgot your password? Get it!</div>
  </div>
</section>

<section>
  <h2 class="abs section-head" style="left:81px;top:422px">Latest Deals</h2>
  <div class="abs section-rule" style="left:186px;top:432px;width:342px"></div>

  <div class="abs deal" style="left:79px;top:458px"><div class="pic seeds" role="img" aria-label="Photo of mixed seeds and grains"></div><div class="price">Now $7.30<svg width="16" height="13" viewBox="0 0 16 13"><path d="M0 1h3l2 8h9l2-6H4" fill="none" stroke="#6cb52d" stroke-width="2"/><circle cx="6" cy="11.5" r="1.4" fill="#6cb52d"/><circle cx="13" cy="11.5" r="1.4" fill="#6cb52d"/></svg></div></div>
  <div class="abs deal" style="left:246px;top:458px"><div class="pic bottle" role="img" aria-label="Photo of a bottle of probiotic supplement"></div><div class="price">Now $7.30<svg width="16" height="13" viewBox="0 0 16 13"><path d="M0 1h3l2 8h9l2-6H4" fill="none" stroke="#6cb52d" stroke-width="2"/><circle cx="6" cy="11.5" r="1.4" fill="#6cb52d"/><circle cx="13" cy="11.5" r="1.4" fill="#6cb52d"/></svg></div></div>
  <div class="abs deal" style="left:412px;top:458px"><div class="pic almonds" role="img" aria-label="Photo of raw almonds"></div><div class="price">Now $7.30<svg width="16" height="13" viewBox="0 0 16 13"><path d="M0 1h3l2 8h9l2-6H4" fill="none" stroke="#6cb52d" stroke-width="2"/><circle cx="6" cy="11.5" r="1.4" fill="#6cb52d"/><circle cx="13" cy="11.5" r="1.4" fill="#6cb52d"/></svg></div></div>
</section>

<section>
  <h2 class="abs section-head" style="left:81px;top:616px">Latest News</h2>
  <div class="abs section-rule" style="left:186px;top:626px;width:342px"></div>

  <article class="abs news" style="left:80px;top:654px"><div class="pic pantry" role="img" aria-label="Black and white photo of a pantry with jars and produce"></div><p>Lorem Ipsum is simply dummy text of the printing and type-setting industry. Lorem Ipsum</p><a>Readmore...</a></article>
  <article class="abs news" style="left:241px;top:654px"><div class="pic balls" role="img" aria-label="Photo of coconut bliss balls on a plate"></div><p>Lorem Ipsum is simply dummy text of the printing and type-setting industry. Lorem Ipsum</p><a>Readmore...</a></article>
  <article class="abs news" style="left:406px;top:652px"><div class="pic grain" role="img" aria-label="Photo of buckwheat grains"></div><p>Lorem Ipsum is simply dummy text of the printing and type-setting industry. Lorem Ipsum</p><a>Readmore...</a></article>

  <article class="abs news" style="left:81px;top:851px"><div class="pic pantry" role="img" aria-label="Black and white photo of a pantry with jars and produce"></div><p>Lorem Ipsum is simply dummy text of the printing and type-setting industry. Lorem Ipsum</p><a>Readmore...</a></article>
  <article class="abs news" style="left:240px;top:850px"><div class="pic balls" role="img" aria-label="Photo of coconut bliss balls on a plate"></div><p>Lorem Ipsum is simply dummy text of the printing and type-setting industry. Lorem Ipsum</p><a>Readmore...</a></article>
  <article class="abs news" style="left:406px;top:849px"><div class="pic grain" role="img" aria-label="Photo of buckwheat grains"></div><p>Lorem Ipsum is simply dummy text of the printing and type-setting industry. Lorem Ipsum</p><a>Readmore...</a></article>
</section>

<aside>
  <div class="abs tab" style="left:612px;top:418px">Product Categories</div>
  <ul class="abs cats" style="left:604px;top:442px">
    <li>Alternative goods</li><li>Dairy Free</li><li>Gluten Free</li><li>Grocery</li><li>Health Supplements</li><li>Natural Grocer</li><li>Organic</li><li>Recipes</li><li>Seasonal</li><li>Sugar Replacements</li>
  </ul>
  <div class="abs tab" style="left:612px;top:720px">By Weight Categories</div>
  <ul class="abs cats" style="left:604px;top:744px;padding-top:6px">
    <li>Baking</li><li>Beans &amp; Peas</li><li>Candy &amp; Sweet Treats</li><li>Cereals &amp; Granolas</li><li>Coffee &amp; Tea</li><li>Dried Fruit</li><li>Free Range Meat</li><li>Gluten Free Processed Meat</li><li>Pasture Fed Beef</li><li>Pasture Grazed Lamb</li><li>Preservative Free Meat</li>
  </ul>
</aside>

<section>
  <div class="abs sub-title">Subscribe <span>Newsletter</span></div>
  <div class="abs sub-input" style="left:219px">your name</div>
  <div class="abs sub-input" style="left:470px">mail@yourmail.com</div>
  <div class="abs submit">SUBMIT</div>
</section>

<footer>
  <div class="abs footer"></div>
  <div class="abs foot-links">HOME &nbsp; | &nbsp;SHOP &nbsp; | &nbsp;PURCHASE BY WEIGHT &nbsp; | &nbsp;RECIPES &nbsp; | &nbsp;BLOG &nbsp; | &nbsp;CONTACT US</div>
  <div class="abs copy">© 2014 Marlowvale Wholefoods Company. &nbsp;All rights reserved. &nbsp;Privacy Policy &nbsp;| &nbsp;Terms of Use</div>
  <div class="abs cards"><span></span><span></span><span></span><span></span><span></span><span class="wide"></span></div>
  <div class="abs area"><div class="name">Fernhollow</div><div class="tag">Sustainable Business</div></div>
</footer>

</body>
</html>
```